Pine Ridge Traders, LLC- Global Beverage Company with 100% Cold Chain Logistics

Hey All, My Name is Tom, I am a young business owner in a competitive export space, but my niche is that I am shipping all of my beer around the world, "100% Cold Chain". This model is more costly, but it protects the integrity of the beer itself and will give folks in foreign countries the best representation of what US Craft Beer has to offer.

I am not a branding guy and don't claim to be one, I am a salesperson first, and will be referring to all of you to create something great that will be memorable.

I am looking for a basic Business Card Design for my Craft Beer Export company. I sell US Craft Beer in several countries around the globe. Austrailia, China, Taiwan, Chile, France, New Zealand... to name a few.

I am looking for a sleek, modern, and fresh design. Quickly!

Thanks for your consideration!

Cheers,

Tom

Target Market(s)

International

Contact Information for Business Card

Tom Reilly
Founder- World Brew Guy
Tom@PineRidgeTraders.example
@WorldBrewGuy- Instagram only
www.Pineridgetraders.example
@PineRidgeTradersAU- Instagram Only

Font styles to use
Serif

Colors
0592cd
ffffff

Requirements
Must have
• Name-
• Title-
• Email-
• Social Media Handle-
• Company Website-
Nice to have
• Nice Logo/ Images on Card
Should not have
• Tacky Beer Images

```html
<!DOCTYPE html>
<html lang="en">
<head>
<meta charset="utf-8">
<title>Pine Ridge Traders – Business Card</title>
<link href="https://fonts.googleapis.com/css2?family=Cinzel:wght@400;600;700&family=Roboto:wght@400&display=swap" rel="stylesheet">
<style>
  :root {
    --backdrop: #ebe6de;
    --kraft-light: #cfa574;
    --kraft-dark: #b98a59;
    --ink: #1a1410;
    --rule: #3b2e22;
  }
  * { box-sizing: border-box; margin: 0; padding: 0; }
  html, body {
    width: 1200px; height: 900px; overflow: hidden;
    background: var(--backdrop);
  }
  .canvas { position: relative; width: 1200px; height: 900px; }
  .card {
    position: absolute;
    background: linear-gradient(135deg, var(--kraft-light), var(--kraft-dark));
    color: var(--ink);
    text-align: center;
    box-shadow: 0 2px 6px rgba(0,0,0,0.25);
  }
  .card--front { left: 330px; top: 90px; width: 555px; height: 343px; }
  .card--back  { left: 330px; top: 470px; width: 558px; height: 342px; }

  .person-name {
    position: absolute; left: 0; right: 0; top: 66px;
    font: 400 27px/1 "Cinzel", serif; letter-spacing: 0.5px;
  }
  .person-title {
    position: absolute; left: 0; right: 0; top: 101px;
    font: 400 16px/1 "Roboto", sans-serif;
  }
  .divider {
    position: absolute; left: 0; right: 0;
    display: flex; justify-content: center; align-items: center; gap: 10px;
  }
  .divider__rule { width: 62px; height: 1px; background: var(--rule); }
  .divider--contact { top: 146px; }
  .divider--social { top: 233px; }
  .divider__icons { display: flex; gap: 4px; }
  .contact-line {
    position: absolute; left: 0; right: 0;
    font: 400 16px/1 "Roboto", sans-serif;
  }
  .contact-line--email { top: 173px; }
  .contact-line--web { top: 193px; }
  .contact-line--handle { top: 262px; }

  .tagline {
    position: absolute; left: 0; right: 0; top: 40px;
    font: 700 21px/1 "Cinzel", serif; letter-spacing: 0.3px;
  }
  .brand-mark {
    position: absolute; left: 249px; top: 90px; width: 60px; height: 60px;
    background: var(--ink);
  }
  .brand-name {
    position: absolute; left: 0; right: 0; top: 180px;
    font: 400 31px/1 "Cinzel", serif; letter-spacing: 1px;
  }
  .brand-descriptor {
    position: absolute; left: 0; right: 0; top: 243px;
    font: 400 15px/1 "Cinzel", serif; letter-spacing: 2px;
  }
  .brand-rule {
    position: absolute; left: 145px; width: 268px; top: 226px; height: 2px;
    background: var(--ink);
  }
  .markets {
    position: absolute; left: 0; right: 0; top: 289px;
    font: 400 16px/1 "Roboto", sans-serif;
  }
</style>
</head>
<body>
<main class="canvas">

  <section class="card card--front" aria-label="Card front">
    <h1 class="person-name">Tom Reilly</h1>
    <p class="person-title">Founder - World Brew Guy</p>

    <div class="divider divider--contact">
      <span class="divider__rule"></span>
      <span class="divider__icons">
        <svg width="15" height="12" viewBox="0 0 15 12" aria-label="Email">
          <rect x="0" y="0" width="15" height="12" fill="var(--ink)"/>
          <path d="M0.8 1 L7.5 6.5 L14.2 1" fill="none" stroke="var(--kraft-light)" stroke-width="1.2"/>
        </svg>
        <svg width="14" height="14" viewBox="0 0 14 14" aria-label="Website">
          <circle cx="7" cy="7" r="6.5" fill="var(--ink)"/>
          <path d="M4 4 Q6 3 7 5 Q6 7 4 7 Z M8 8 Q10 7 11 9 Q10 11 8 11 Z" fill="var(--kraft-light)"/>
        </svg>
      </span>
      <span class="divider__rule"></span>
    </div>

    <p class="contact-line contact-line--email">Tom@PineRidgeTraders.example</p>
    <p class="contact-line contact-line--web">www.Pineridgetraders.example</p>

    <div class="divider divider--social">
      <span class="divider__rule"></span>
      <svg width="22" height="22" viewBox="0 0 22 22" aria-label="Social profile">
        <circle cx="11" cy="11" r="10" fill="none" stroke="var(--ink)" stroke-width="1.3"/>
      </svg>
      <span class="divider__rule"></span>
    </div>
    <p class="contact-line contact-line--handle">@WorldBrewGuy</p>
  </section>

  <section class="card card--back" aria-label="Card back">
    <h2 class="tagline">100% Cold Chain Logistics</h2>
    <span class="brand-mark" aria-hidden="true"></span>
    <p class="brand-name">PINE RIDGE TRADERS</p>
    <span class="brand-rule" aria-hidden="true"></span>
    <p class="brand-descriptor">GLOBAL BEVERAGE COMPANY</p>
    <p class="markets">AUSTRAILIA | CHINA | TAIWAN | CHILE | FRANCE | NEW ZEALAND</p>
  </section>

</main>
</body>
</html>
```